New business card for our new logo

I have a brand new, existing logo. Now I need it on a new business card. The new card should include the following:

English language training
Translations
Interpreting Services (remote and in-person)

Target Market(s)

We are targeting international companies with foreign investment in the United States as well as domestic companies, medical offices, law offices, and non-profits that have non-native English speakers as their clients.

Contact Information for Business Card

Delia Brancombe, President
418 Garrow St.
Lindenport, IN 46815
(317) 548-3162
info@tallpinewordworks.com
www.tallpinewordworks.com

Font styles to use
Sans Serif

Colors
0392cd
3176b5
abd036
9bcb3b
f04a50
f78f20

Requirements
Must have
• It must include our logo and business card details
Nice to have
• I would like to see a layout that is uncluttered and conveys trust and dependability, as well as the feelings of being friendly and approachable.

It would be nice to have icons for English language training, translating, and interpreting.
Should not have
• No pink, yellow, or purple

```html
<!DOCTYPE html>
<html lang="en">
<head>
<meta charset="utf-8">
<title>Tall Pine Wordworks – Business Card</title>
<link href="https://fonts.googleapis.com/css2?family=Montserrat:wght@600;700&family=Mulish:wght@400;600&display=swap" rel="stylesheet">
<style>
  :root {
    --bg: #e6e6e6;
    --card: #f4f4f4;
    --band: #dcdcdc;
    --blue: #1a6fe0;
    --red: #e8474f;
    --ink: #222222;
    --text: #2e2e2e;
  }
  * { box-sizing: border-box; margin: 0; padding: 0; }
  html, body { width: 1200px; height: 794px; overflow: hidden; }
  body {
    background: var(--bg);
    font-family: "Mulish", sans-serif;
    position: relative;
  }
  .card {
    position: absolute;
    top: 242px;
    width: 540px;
    height: 309px;
    background: var(--card);
    box-shadow: 0 6px 18px rgba(0,0,0,0.12);
    overflow: hidden;
  }
  .card--services { left: 40px; }
  .card--contact { left: 620px; }

  /* brand lockup */
  .brand { display: flex; align-items: center; gap: 14px; }
  .brand__dot {
    width: 78px; height: 78px; border-radius: 50%;
    background: var(--blue); flex: none;
  }
  .brand__name {
    font-family: "Montserrat", sans-serif;
    font-weight: 700;
    color: var(--blue);
    font-size: 21px;
    line-height: 1.02;
  }
  .card--services .brand {
    position: absolute; left: 0; right: 0; top: 48px;
    justify-content: center;
  }

  /* services band */
  .services {
    position: absolute; left: 0; right: 0; bottom: 0; height: 126px;
    background: var(--band);
    display: flex; align-items: center;
  }
  .service {
    flex: 1; display: flex; flex-direction: column; align-items: center; gap: 10px;
  }
  .service svg { width: 34px; height: 30px; }
  .service__label {
    font-family: "Mulish", sans-serif; font-weight: 600;
    font-size: 13px; letter-spacing: 0.02em; color: var(--blue);
    text-transform: uppercase;
  }
  .services__divider { width: 1.5px; height: 46px; background: var(--red); }

  /* contact card */
  .card__stripe { position: absolute; left: 0; right: 0; top: 0; height: 8px; background: var(--blue); }
  .card--contact .brand { position: absolute; right: 40px; top: 44px; gap: 12px; }
  .card--contact .brand__dot { width: 70px; height: 70px; }
  .card--contact .brand__name { font-size: 18px; }
  .person { position: absolute; left: 44px; top: 140px; }
  .person__name {
    font-family: "Montserrat", sans-serif; font-weight: 700;
    color: var(--blue); font-size: 19px; text-transform: uppercase; letter-spacing: 0.01em;
  }
  .person__title {
    font-family: "Montserrat", sans-serif; font-weight: 700;
    color: var(--ink); font-size: 15px; margin-top: 2px;
  }
  .contact-list { position: absolute; left: 44px; top: 196px; list-style: none; }
  .contact-list li {
    display: flex; align-items: flex-start; gap: 12px;
    font-size: 13.5px; line-height: 20px; color: var(--text);
    text-transform: uppercase; letter-spacing: 0.01em;
  }
  .contact-list svg { width: 15px; height: 15px; margin-top: 2px; flex: none; }
</style>
</head>
<body>

<section class="card card--services" aria-label="Card front – services">
  <div class="brand">
    <span class="brand__dot"></span>
    <span class="brand__name">Tall Pine<br>Wordworks</span>
  </div>
  <div class="services">
    <div class="service">
      <svg viewBox="0 0 34 30" fill="none" stroke="var(--blue)" stroke-width="1.6">
        <rect x="2" y="2" width="13" height="12" rx="2"/>
        <rect x="19" y="14" width="13" height="12" rx="2"/>
        <path d="M6 11 L8.5 5 L11 11 M7 9 H10"/>
        <path d="M22 18 H29 M25.5 17 V23 M23 23 L28 19"/>
        <path d="M17 6 H23 V11 M21 9 L23 11 L25 9"/>
      </svg>
      <span class="service__label">Translating</span>
    </div>
    <span class="services__divider"></span>
    <div class="service">
      <svg viewBox="0 0 34 30" fill="none" stroke="var(--blue)" stroke-width="1.6">
        <rect x="12" y="3" width="20" height="13" rx="1"/>
        <path d="M22 16 V22 M17 27 L22 22 L27 27"/>
        <circle cx="6" cy="8" r="3"/>
        <path d="M2 27 V15 H10 L14 11"/>
      </svg>
      <span class="service__label">Training</span>
    </div>
    <span class="services__divider"></span>
    <div class="service">
      <svg viewBox="0 0 34 30" fill="none" stroke="var(--blue)" stroke-width="1.6">
        <rect x="2" y="3" width="14" height="9" rx="2"/>
        <rect x="18" y="9" width="14" height="9" rx="2"/>
        <circle cx="9" cy="19" r="3"/>
        <path d="M3 28 Q9 21 15 28"/>
        <path d="M22 28 H32"/>
      </svg>
      <span class="service__label">Interpreting</span>
    </div>
  </div>
</section>

<section class="card card--contact" aria-label="Card back – contact details">
  <div class="card__stripe"></div>
  <div class="brand">
    <span class="brand__dot"></span>
    <span class="brand__name">Tall Pine<br>Wordworks</span>
  </div>
  <div class="person">
    <div class="person__name">Delia Brancombe</div>
    <div class="person__title">President</div>
  </div>
  <ul class="contact-list">
    <li>
      <svg viewBox="0 0 16 16" fill="none" stroke="var(--red)" stroke-width="1.3"><rect x="4" y="1" width="8" height="14" rx="1.5"/><path d="M7 12.5 H9"/></svg>
      (317) 548-3162
    </li>
    <li>
      <svg viewBox="0 0 16 16" fill="none" stroke="var(--red)" stroke-width="1.3"><rect x="1" y="3" width="14" height="10" rx="1"/><path d="M1 3 L8 9 L15 3"/></svg>
      info@tallpinewordworks.com
    </li>
    <li>
      <svg viewBox="0 0 16 16" fill="none" stroke="var(--red)" stroke-width="1.3"><circle cx="8" cy="8" r="6.5"/><ellipse cx="8" cy="8" rx="3" ry="6.5"/><path d="M1.5 8 H14.5"/></svg>
      www.tallpinewordworks.com
    </li>
    <li>
      <svg viewBox="0 0 16 16" fill="none" stroke="var(--red)" stroke-width="1.3"><path d="M8 14 C4 9 3.5 7.5 3.5 6 A4.5 4.5 0 0 1 12.5 6 C12.5 7.5 12 9 8 14 Z"/><circle cx="8" cy="6" r="1.6"/></svg>
      <span>418 Garrow St.<br>Lindenport, IN 46815</span>
    </li>
  </ul>
</section>

</body>
</html>
```